Small business updating business cards

We have already updated our logo via Pixel Forum and downloaded it (hopefully) for you to use. Now an updated set of business cards for Neil Pollard and Stuart Pollard are also needed... we are also hoping that a copy of our outdated business card designs have uploaded successfully as Microsoft Publisher files. Our Strength Through Unity motto has died a slow death so we are hoping to remove it (and other superfluous lingo if the graphic covers the idea) and instead opt for a fancy graphic (?) on the second side of the card that really reflects our desire to obtain product / haulage from Road Transport / Yard Operators and convert legs of their haulage to rail freight where profitable (bulk haulage / containterised etc). Can you help us look larger, bolder and more robust than we really are (two man show)?
Target Market(s)
Transport Industry
Industry/Entity Type
Business
Contact Information for Business Card
Card details for both N Pollard and S Pollard have been uploaded on the publisher files
Colors
Designer to choose colors to be used in the design.
Requirements
Must have
- Similar theme both sides of card
Should not have
- Black on one side white on the other

```html
<!DOCTYPE html>
<html lang="en">
<head>
<meta charset="utf-8">
<title>Tallowrail – Business Card</title>
<link href="https://fonts.googleapis.com/css2?family=Roboto:wght@400;500;700&display=swap" rel="stylesheet">
<style>
  :root {
    --page: #e6e3df;
    --card: #131313;
    --white: #ffffff;
    --soft-white: #e9e9e9;
    --teal: #2a93b3;
    --gold: #d9a633;
  }
  * { margin: 0; padding: 0; box-sizing: border-box; }
  html, body {
    width: 1200px;
    height: 1200px;
    overflow: hidden;
    background: var(--page);
    font-family: "Roboto", Arial, sans-serif;
  }
  .card {
    position: absolute;
    left: 214px;
    width: 772px;
    height: 440px;
    background: var(--card);
    box-shadow: 0 3px 10px rgba(0,0,0,0.25);
  }
  .card--front { top: 150px; }
  .card--back { top: 633px; }

  .brand-name {
    position: absolute;
    color: var(--teal);
    font-weight: 700;
    letter-spacing: -0.5px;
    white-space: nowrap;
    line-height: 1;
  }
  .card--front .brand-name {
    left: 51px;
    top: 188px;
    font-size: 68px;
  }
  .card--back .brand-name {
    left: 0;
    width: 100%;
    text-align: center;
    top: 172px;
    font-size: 110px;
  }

  .divider {
    position: absolute;
    left: 388px;
    top: 97px;
    width: 2px;
    height: 246px;
    background: linear-gradient(to bottom, var(--teal), var(--gold));
  }

  .contact {
    position: absolute;
    left: 424px;
    top: 92px;
    color: var(--white);
  }
  .contact__name {
    font-size: 29px;
    font-weight: 700;
    letter-spacing: 0.3px;
    line-height: 1;
  }
  .contact__role {
    margin-top: 6px;
    font-size: 20px;
    color: var(--soft-white);
  }
  .contact__address {
    margin-top: 31px;
    font-size: 19px;
    line-height: 26px;
    color: var(--soft-white);
  }
  .contact__list {
    list-style: none;
    margin-top: 14px;
  }
  .contact__item {
    display: flex;
    align-items: center;
    height: 28px;
    font-size: 15.5px;
    color: var(--soft-white);
  }
  .contact__item--strong {
    font-size: 19px;
    font-weight: 500;
    color: var(--white);
  }
  .contact__icon {
    width: 18px;
    height: 18px;
    margin-right: 6px;
    flex: none;
  }

  .website {
    position: absolute;
    left: 0;
    width: 100%;
    top: 384px;
    text-align: center;
    color: var(--soft-white);
    font-size: 20px;
    letter-spacing: 0.3px;
  }
</style>
</head>
<body>

<section class="card card--front">
  <div class="brand-name">Tallowrail</div>
  <div class="divider"></div>
  <div class="contact">
    <h1 class="contact__name">STUART POLLARD</h1>
    <p class="contact__role">Director</p>
    <p class="contact__address">14 Carrow Street<br>Tenby NSW 2871</p>
    <ul class="contact__list">
      <li class="contact__item contact__item--strong">
        <svg class="contact__icon" viewBox="0 0 18 18" aria-hidden="true">
          <rect x="4.5" y="1" width="9" height="16" rx="1.5" fill="none" stroke="var(--gold)" stroke-width="1.4"/>
          <line x1="7.5" y1="14.5" x2="10.5" y2="14.5" stroke="var(--gold)" stroke-width="1.2"/>
        </svg>
        0491 570 156
      </li>
      <li class="contact__item contact__item--strong">
        <svg class="contact__icon" viewBox="0 0 18 18" aria-hidden="true">
          <rect x="1.5" y="4" width="15" height="10" fill="none" stroke="var(--gold)" stroke-width="1.2"/>
          <polyline points="1.5,4 9,10 16.5,4" fill="none" stroke="var(--gold)" stroke-width="1.2"/>
        </svg>
        pollards@tallowrail.com.au
      </li>
      <li class="contact__item">
        <svg class="contact__icon" viewBox="0 0 18 18" aria-hidden="true">
          <rect x="1.5" y="4" width="15" height="10" fill="none" stroke="var(--gold)" stroke-width="1.2"/>
          <polyline points="1.5,4 9,10 16.5,4" fill="none" stroke="var(--gold)" stroke-width="1.2"/>
        </svg>
        tallowrail@inboxly.net (Alternate)
      </li>
      <li class="contact__item">
        <svg class="contact__icon" viewBox="0 0 18 18" aria-hidden="true">
          <rect x="1.5" y="4" width="15" height="10" fill="none" stroke="var(--gold)" stroke-width="1.2"/>
          <polyline points="1.5,4 9,10 16.5,4" fill="none" stroke="var(--gold)" stroke-width="1.2"/>
        </svg>
        tallowrail@mailnest.net (Alternate)
      </li>
    </ul>
  </div>
</section>

<section class="card card--back">
  <div class="brand-name">Tallowrail</div>
  <p class="website">www.tallowrail.com.au</p>
</section>

</body>
</html>
```